Stayvora Waterfront Home Postcard

Hello

I have recently placed my house on Stayvora and would like to use the very nice pictures I already have available to get postcards for my guests so they have a souvenir and it also becomes a advertisement tool. Can you help me?

Thank you
Marisol

Target Market(s)

Holiday makers looking for a wildlife sanctuary

Industry/Entity Type

House

Font styles to use
Script

Colors

Designer to choose colors to be used in the design.

Requirements
Must have
• Water front Home on one of the Crest Isles near Brisbane beautifully furnished and appointed for $30/night (on the basis of x4 people sharing) sleeps max. 6 people

Book through Stayvora: www.stayvora.example/rooms/4392071 and your friendly host will give you more details
Nice to have
• If it is possible to also have some of the other pictures

```html
<!DOCTYPE html>
<html lang="en">
<head>
<meta charset="utf-8">
<title>Stayvora Waterfront Home Postcard</title>
<link rel="stylesheet" href="https://fonts.googleapis.com/css2?family=Lilita+One&family=Lobster&family=Oswald:wght@400;500&family=PT+Sans:wght@400;700&family=Great+Vibes&display=swap">
<style>
  :root {
    --backdrop: #ece7df;
    --sky: #7fd0e3;
    --sun-yellow: #f7e53a;
    --coral: #f2956b;
    --teal: #80cfdc;
    --teal-deep: #5fb8c8;
    --brown: #6a4d3d;
    --ink: #2b2727;
    --white: #ffffff;
  }
  * { box-sizing: border-box; margin: 0; padding: 0; }
  html, body { width: 1200px; height: 500px; overflow: hidden; }
  body { background: var(--backdrop); position: relative; font-family: "PT Sans", sans-serif; }

  .card { position: absolute; top: 32px; width: 560px; height: 434px; overflow: hidden; box-shadow: 0 3px 10px rgba(0,0,0,.25); }

  /* Front */
  .front { left: 22px; background: var(--sky); }
  .front-title { position: absolute; top: 22px; width: 100%; text-align: center; font-family: "Lilita One", sans-serif; font-size: 24px; color: var(--sun-yellow); letter-spacing: .5px; text-shadow: 1px 2px 2px rgba(0,0,0,.45); }
  .front-sub { position: absolute; top: 56px; width: 100%; text-align: center; font-family: "Lobster", cursive; font-size: 24px; color: var(--sun-yellow); text-shadow: 1px 2px 2px rgba(0,0,0,.5); }
  .front-sub .place { font-size: 30px; }
  .photo { position: absolute; box-shadow: 2px 3px 6px rgba(0,0,0,.45); }
  .photo-sunset { left: 172px; top: 84px; width: 208px; height: 190px; background: radial-gradient(circle at 50% 35%, #f5b04a, #c1471d 45%, #3a1608 100%); }
  .photo-turtle { left: 33px; top: 100px; width: 150px; height: 100px; background: linear-gradient(160deg, #2c5a5a, #0f2a2c); }
  .photo-birds { left: 378px; top: 98px; width: 148px; height: 98px; background: linear-gradient(180deg, #466a3e, #9a8a78 70%, #d8d2c8); }
  .photo-lounge { left: 33px; top: 208px; width: 180px; height: 116px; background: linear-gradient(135deg, #c98a8a, #a0604a 55%, #e4d6c4); }
  .photo-view { left: 196px; top: 230px; width: 180px; height: 118px; background: linear-gradient(180deg, #7fb0d6, #3c7aa6 55%, #3c6a3a); }
  .photo-kitchen { left: 383px; top: 236px; width: 143px; height: 114px; background: linear-gradient(135deg, #e07a3a, #f0e6d8 55%, #b98452); }
  .front-points { position: absolute; left: 30px; top: 315px; color: var(--sun-yellow); font-weight: 700; font-size: 12.5px; line-height: 16px; text-shadow: 1px 1px 1px rgba(0,0,0,.5); }
  .front-note { position: absolute; left: 30px; top: 349px; font-size: 11px; color: var(--ink); }
  .front-book { position: absolute; left: 0; bottom: 0; width: 100%; height: 68px; background: var(--coral); text-align: center; padding-top: 8px; color: var(--ink); }
  .front-book p { font-family: "Great Vibes", cursive; font-size: 21px; line-height: 26px; }
  .front-book span { font-family: "PT Sans", sans-serif; font-size: 16px; }

  /* Back */
  .back { left: 614px; background: var(--white); }
  .band { position: absolute; }
  .back-title { left: 0; top: 22px; width: 560px; height: 42px; background: var(--teal); font-family: "Oswald", sans-serif; font-weight: 500; font-size: 27px; color: var(--ink); letter-spacing: 2.5px; text-align: center; line-height: 42px; }
  .share { left: 0; top: 73px; width: 176px; height: 44px; background: var(--teal); font-family: "Oswald", sans-serif; font-size: 26px; color: var(--white); text-align: center; line-height: 44px; letter-spacing: 1px; }
  .capacity { left: 181px; top: 68px; width: 379px; height: 48px; background: var(--brown); color: var(--white); font-size: 15.5px; line-height: 48px; padding-left: 12px; word-spacing: 1px; }
  .capacity span + span { margin-left: 22px; }
  .price { left: 0; top: 128px; width: 226px; height: 65px; background: var(--teal); color: var(--ink); font-family: "PT Sans", sans-serif; font-weight: 700; padding-left: 20px; line-height: 65px; }
  .price b { font-size: 40px; }
  .price small { font-size: 22px; }
  .features-head { left: 234px; top: 124px; width: 326px; height: 30px; background: var(--brown); color: var(--white); font-family: "Oswald", sans-serif; font-size: 18px; letter-spacing: 5px; line-height: 30px; padding-left: 12px; }
  .features { left: 236px; top: 162px; list-style: none; color: var(--ink); font-weight: 700; font-size: 15px; line-height: 17px; }
  .features li { margin-bottom: 6px; padding-left: 14px; position: relative; }
  .features li::before { content: "\2713"; position: absolute; left: 0; font-weight: 400; }
  .location { left: 0; top: 220px; width: 226px; height: 38px; background: var(--teal); color: var(--ink); font-weight: 700; font-size: 22px; line-height: 38px; padding-left: 16px; }
  .location-name { left: 14px; top: 264px; color: var(--ink); font-weight: 700; font-size: 19px; letter-spacing: .3px; }
  .book { left: 0; top: 296px; width: 560px; height: 56px; background: var(--brown); color: var(--white); font-weight: 700; font-size: 15.5px; line-height: 19px; text-align: center; padding-top: 9px; }
  .thanks { left: 0; top: 352px; width: 560px; height: 82px; background: var(--teal); color: var(--white); font-family: "Great Vibes", cursive; font-size: 20px; line-height: 26px; text-align: center; padding-top: 15px; }
</style>
</head>
<body>
  <section class="card front">
    <h1 class="front-title">YEAR ROUND WATERFRONT VACATION HOME</h1>
    <h2 class="front-sub">on one of the <span class="place">Crest Isles near Brisbane</span></h2>
    <div class="photo photo-sunset" role="img" aria-label="Sunset over the bay with a moored boat and palm silhouette"></div>
    <div class="photo photo-turtle" role="img" aria-label="Turtle swimming close to a hand in clear water"></div>
    <div class="photo photo-birds" role="img" aria-label="Cockatoo and galah on the balcony rail"></div>
    <div class="photo photo-lounge" role="img" aria-label="Bright living room with cane sofa and tall windows"></div>
    <div class="photo photo-view" role="img" aria-label="Water view through the dining room windows with a sailing boat"></div>
    <div class="photo photo-kitchen" role="img" aria-label="Orange kitchen with timber island bench"></div>
    <div class="front-points">&bull;Beautifully Furnished<br>&bull;$30 per Night</div>
    <p class="front-note">(on the basis of x4 people sharing) sleeps max. 6 people</p>
    <div class="front-book">
      <p>Book through Stayvora: <span>www.stayvora.example/rooms</span></p>
      <p>Or Call <span>4392071</span> and your friendly host will give you more details</p>
    </div>
  </section>

  <section class="card back">
    <h1 class="band back-title">WATERFRONT VACATION HOME FOR RENT</h1>
    <div class="band share">- SHARE -</div>
    <div class="band capacity"><span>x4 people sharing</span><span>sleeps max. 6 people</span></div>
    <div class="band price"><b>$30</b><small> /NIGHT</small></div>
    <div class="band features-head">FEATURES:</div>
    <ul class="band features">
      <li>BEAUTIFULLY FURNISHED HOME</li>
      <li>ONE OF THE BEST ISLANDS<br>TO MAKE A SIGHTING</li>
      <li>DOLPHIN FEEDING</li>
    </ul>
    <div class="band location">LOCATION:</div>
    <p class="band location-name">ONE OF THE CREST ISLES NEAR BRISBANE</p>
    <div class="band book">Book through Stayvora: www.stayvora.example/rooms<br>CALL 4392071 and your friendly host will give you more details</div>
    <div class="band thanks">Thank you for visiting with us.<br>We appreciate guests like you.</div>
  </section>
</body>
</html>
```